A stationary and business card desgn for a podiatry clinic

i require a stationary design for letter heads, envelopes, buisness cards.

it is for a new podiatry practise within a medical centre, that deals with all lower limb pathology and injury and foot related problems.

the colour scheme for my exisiting logo is orange blue and white. colours provided below.
i would like a white background for the buisness card.

the final design should portray health and wellbeing in a professional manner that still looks modern but sophisticated.

male and female, off all ethinical backgrounds aged between 30-80 years

Medical

• letter head.
need to include all contact details mentioned below.
need to also include ABN 53120978446

i prefer the logo on the top left hand corner and the contact info on the right. the address can be written in a sentence like form as the footer.

Business card
Front:

include logo provided.

clinic details on the front of the card.

Delphine Carrow
B.Pod

P: 7394 5186
F: 7394 5130
M: 0437 612 908
E: delphine@tavrin.com.au
W: www.tavrin.com.au

(may use icons to indicate contact type)

on back

Appointments:

lines to write dates, time etc.
(3-4 of these)
and a small photo of just the foot from the logo in coloured watermark.

Address:
Brackwell Medical Centre
47 Tallowin Street
Brackwell SA 5174
(this location infomation could be in smaller font at the bottom of the buisness card under a line, running in a sentence like fashion) or in the bottom left or right hand corner in a paragraph like you would write it on an envelope

however if you think a different lay out at the back will look better by all means i just need to have room for the appointment even if it is just lines/ space.

i also prefer square cards not rounded corners.

thanks
• plain texts such as times new roman and arial

```html
<!DOCTYPE html>
<html lang="en">
<head>
<meta charset="utf-8">
<title>Tavrin Podiatry – Stationery</title>
<link href="https://fonts.googleapis.com/css2?family=Open+Sans:wght@400;600;700&display=swap" rel="stylesheet">
<style>
  :root {
    --brand-blue: #27399a;
    --brand-orange: #f26522;
    --paper: #ffffff;
    --ink: #333333;
    --rule: #c8c8c8;
    --window: #e9e9ea;
    --shadow: 3px 4px 7px rgba(0,0,0,.32);
  }
  * { box-sizing: border-box; margin: 0; padding: 0; }
  html, body { width: 1200px; height: 982px; overflow: hidden; background: #ffffff; }
  body { position: relative; font-family: "Open Sans", Arial, sans-serif; color: var(--ink); }

  .sheet { position: absolute; background: var(--paper); box-shadow: var(--shadow); overflow: hidden; }

  .brand { position: absolute; display: flex; align-items: flex-start; gap: 6px; }
  .brand-dot { width: 14px; height: 14px; border-radius: 50%; background: var(--brand-orange); flex: none; margin-top: 4px; }
  .brand-name { font-weight: 700; color: var(--brand-blue); line-height: 1; letter-spacing: -0.5px; }

  .contact-list { list-style: none; }
  .contact-list li { white-space: nowrap; }
  .contact-list b { color: var(--brand-orange); font-weight: 700; }

  /* Letterhead */
  .letterhead { left: 24px; top: 24px; width: 661px; height: 934px; }
  .letterhead .brand { left: 26px; top: 40px; }
  .letterhead .brand-name { font-size: 40px; }
  .letterhead .sender { position: absolute; left: 426px; top: 43px; }
  .letterhead .sender-name { font-size: 11.5px; font-weight: 700; color: #111; }
  .letterhead .sender-title { font-size: 9px; }
  .letterhead .contact-list { position: absolute; left: 525px; top: 43px; font-size: 8.5px; line-height: 12.2px; padding-left: 8px; border-left: 1.5px dotted var(--brand-blue); }
  .letterhead .footer { position: absolute; left: 0; right: 0; top: 900px; text-align: center; font-size: 9px; color: #444; }
  .letterhead .footer span { margin: 0 6px; color: #888; }

  /* Cards */
  .card { width: 284px; height: 174px; }
  .card-front { left: 491px; top: 177px; }
  .card-front .brand { left: 12px; top: 14px; }
  .card-front .brand-name { font-size: 22px; }
  .card-front .brand-dot { width: 9px; height: 9px; margin-top: 3px; }
  .card-front .holder { position: absolute; left: 12px; top: 72px; }
  .card-front .holder-name { font-size: 11.5px; font-weight: 700; color: #111; }
  .card-front .holder-title { font-size: 8.5px; }
  .card-front .contact-list { position: absolute; left: 12px; top: 103px; font-size: 8px; line-height: 12.2px; }
  .card-art { position: absolute; right: 0; top: 0; width: 124px; height: 174px; }

  .card-back { left: 491px; top: 368px; height: 171px; }
  .card-back .heading { position: absolute; left: 12px; top: 8px; font-size: 11.5px; color: #222; }
  .appt-lines { position: absolute; left: 12px; top: 43px; width: 138px; }
  .appt-lines span { display: block; height: 22px; border-top: 1px solid var(--rule); }
  .card-back address { position: absolute; left: 12px; top: 123px; font-style: normal; font-size: 7.5px; line-height: 12px; }

  /* Envelope */
  .envelope { left: 485px; top: 559px; width: 693px; height: 344px; }
  .envelope .brand { left: 24px; top: 28px; }
  .envelope .brand-name { font-size: 26px; }
  .envelope .brand-dot { width: 10px; height: 10px; margin-top: 3px; }
  .envelope .guide { position: absolute; left: 25px; top: 89px; height: 230px; border-left: 1.5px dotted var(--brand-blue); }
  .envelope .window { position: absolute; left: 57px; top: 158px; width: 281px; height: 123px; background: var(--window); border: 1px solid #555; border-radius: 10px; }
  .envelope .return-line { position: absolute; left: 30px; top: 311px; font-size: 7.5px; }
</style>
</head>
<body>

  <section class="sheet letterhead" aria-label="Letterhead">
    <div class="brand"><span class="brand-name">Tavrin<br>Podiatry</span><span class="brand-dot"></span></div>
    <div class="sender">
      <p class="sender-name">Delphine Carrow</p>
      <p class="sender-title">B.Pod</p>
    </div>
    <ul class="contact-list">
      <li><b>p:</b> 7394 5186</li>
      <li><b>f:</b> 7394 5130</li>
      <li><b>m:</b> 0437 612 908</li>
      <li><b>e:</b> delphine@tavrin.com.au</li>
      <li><b>w:</b> www.tavrin.com.au</li>
    </ul>
    <p class="footer">Brackwell Medical Centre, 47 Tallowin Street, Brackwell, SA 5174<span>|</span>ABN 53120978446</p>
  </section>

  <section class="sheet card card-front" aria-label="Business card front">
    <div class="brand"><span class="brand-name">Tavrin<br>Podiatry</span><span class="brand-dot"></span></div>
    <div class="holder">
      <p class="holder-name">Delphine Carrow</p>
      <p class="holder-title">B.Pod</p>
    </div>
    <ul class="contact-list">
      <li><b>p:</b> 7394 5186</li>
      <li><b>f:</b> 7394 5130</li>
      <li><b>m:</b> 0437 612 908</li>
      <li><b>e:</b> delphine@tavrin.com.au</li>
      <li><b>w:</b> www.tavrin.com.au</li>
    </ul>
    <svg class="card-art" viewBox="0 0 124 174" role="img" aria-label="Large brand symbol decoration in orange and blue">
      <defs>
        <linearGradient id="frontArt" x1="0" y1="0" x2="0" y2="1">
          <stop offset="0" stop-color="#f26522" stop-opacity=".85"/>
          <stop offset="1" stop-color="#27399a" stop-opacity=".85"/>
        </linearGradient>
      </defs>
      <rect x="0" y="0" width="124" height="174" fill="url(#frontArt)" opacity=".9"/>
    </svg>
  </section>

  <section class="sheet card card-back" aria-label="Appointment card">
    <p class="heading">Appointments</p>
    <div class="appt-lines"><span></span><span></span><span></span><span></span></div>
    <address>Brackwell Medical Centre<br>47 Tallowin Street<br>Brackwell SA 5174</address>
    <svg class="card-art" viewBox="0 0 124 171" role="img" aria-label="Faint watermark of the brand foot symbol">
      <defs>
        <linearGradient id="backArt" x1="0" y1="0" x2="0" y2="1">
          <stop offset="0" stop-color="#fbe3d6"/>
          <stop offset="1" stop-color="#e2e3f2"/>
        </linearGradient>
      </defs>
      <rect x="0" y="0" width="124" height="171" fill="url(#backArt)"/>
    </svg>
  </section>

  <section class="sheet envelope" aria-label="Window envelope">
    <div class="brand"><span class="brand-name">Tavrin<br>Podiatry</span><span class="brand-dot"></span></div>
    <span class="guide"></span>
    <div class="window"></div>
    <p class="return-line">Brackwell Medical Centre, 47 Tallowin Street, Brackwell SA 5174</p>
  </section>

</body>
</html>
```